We need a full website with logo/graphics/woocommerce for hemp-based company

This site will be velmorix.com. It is a website featuring the fact we are the only manufacturer to produce CBDP and THCP. It should be great on mobile and desktop. We will pay for any extensions needed and while it should be a simple site:

About Us
About the Laboratory
About CBDP
About THCP
Shop
Contact Us

Only 4 products on the site.

It can be wordpress or joomla. Your choice. You must install the final website on our server. We agree to pay for monthly support that must be submitted in your quote.

He have a great graphics designer that will assist keeping colors and graphics clean according to your specifications.

Industry/Entity Type

Hemp CBD THC

Coding

Coded - Design and coding required

Number of Pages Required

5+ page

Requirements
Must have
• A simple clean layout

```html
<!DOCTYPE html>
<html lang="en">
<head>
<meta charset="utf-8">
<title>Velmorix</title>
<link href="https://fonts.googleapis.com/css2?family=Open+Sans:wght@300;400;600;700&display=swap" rel="stylesheet">
<style>
  :root {
    --ink-white: #ffffff;
    --brand-green: #1f9a5c;
    --nav-text: #f1efe9;
    --divider: rgba(255,255,255,0.22);
    --bg-dark: #1d1f1a;
    --page: #ffffff;
  }
  * { margin: 0; padding: 0; box-sizing: border-box; }
  html, body { width: 1200px; height: 587px; overflow: hidden; background: var(--page); }
  body { font-family: "Open Sans", sans-serif; position: relative; }

  .hero-photo {
    position: absolute; inset: 0;
    background:
      radial-gradient(ellipse 380px 260px at 860px 400px, rgba(110,150,60,0.85), transparent 70%),
      radial-gradient(ellipse 300px 200px at 1150px 80px, rgba(95,140,60,0.9), transparent 70%),
      radial-gradient(ellipse 260px 160px at 560px 130px, rgba(150,80,40,0.55), transparent 70%),
      linear-gradient(180deg, #1e1f18 0%, #3a3324 38%, #8a7c62 62%, #9c8d73 80%, #a39579 100%);
  }

  .site-header {
    position: absolute; top: 0; left: 0; right: 0; height: 49px;
    border-bottom: 1px solid rgba(255,255,255,0.12);
  }
  .brand {
    position: absolute; left: 256px; top: 8px;
    display: flex; align-items: center; gap: 9px;
    color: var(--ink-white); font-weight: 700; font-size: 22px; letter-spacing: 0.3px;
  }
  .brand-dot { width: 30px; height: 30px; border-radius: 50%; background: var(--brand-green); }
  .main-nav {
    position: absolute; left: 484px; top: 13px;
    display: flex;
  }
  .main-nav a {
    color: var(--nav-text); text-decoration: none; font-size: 10px;
    padding: 4px 9px; border-right: 1px solid var(--divider);
  }
  .main-nav a:last-child { border-right: none; }
  .header-icons { position: absolute; left: 894px; top: 14px; display: flex; gap: 19px; }
  .cart { position: relative; }
  .cart-count {
    position: absolute; top: -5px; right: -8px; width: 10px; height: 10px; border-radius: 50%;
    background: var(--brand-green); color: #fff; font-size: 6.5px; font-weight: 700;
    display: flex; align-items: center; justify-content: center;
  }

  .hero-copy { position: absolute; left: 250px; top: 180px; width: 380px; }
  .hero-title { color: var(--ink-white); font-weight: 700; font-size: 29px; line-height: 36px; }
  .hero-tagline { color: var(--brand-green); font-weight: 700; font-size: 29px; line-height: 36px; }
  .hero-text {
    margin-top: 13px; color: var(--ink-white); font-weight: 300;
    font-size: 11px; line-height: 15.2px; width: 370px;
  }
  .btn-learn {
    margin-top: 23px; display: inline-flex; align-items: center; gap: 6px;
    width: 117px; height: 27px; justify-content: center;
    border: 1px solid rgba(255,255,255,0.85); border-radius: 2px;
    color: var(--ink-white); font-weight: 700; font-size: 9px; letter-spacing: 0.6px;
    text-decoration: none;
  }

  .hero-wave { position: absolute; left: 0; bottom: 0; width: 1200px; height: 100px; }
</style>
</head>
<body>
  <div class="hero-photo" role="img" aria-label="Amber dropper bottle and a small glass vial of oil on burlap beside fresh hemp leaves"></div>

  <header class="site-header">
    <div class="brand"><span class="brand-dot"></span>Velmorix</div>
    <nav class="main-nav">
      <a href="#">About Us</a>
      <a href="#">About The Laboratory</a>
      <a href="#">About CBDP</a>
      <a href="#">About THCP</a>
      <a href="#">Contact Us</a>
    </nav>
    <div class="header-icons">
      <svg width="12" height="12" viewBox="0 0 12 12" aria-label="Account">
        <circle cx="6" cy="3.3" r="3" fill="#fff"/>
        <path d="M0.5 12 C0.5 8 2.5 7 6 7 C9.5 7 11.5 8 11.5 12 Z" fill="#fff"/>
      </svg>
      <span class="cart">
        <svg width="14" height="12" viewBox="0 0 14 12" aria-label="Cart">
          <path d="M0 4.5 H14 V6 H13 L11.8 12 H2.2 L1 6 H0 Z" fill="#fff"/>
          <path d="M3 4.5 L5.5 0.5 M11 4.5 L8.5 0.5" stroke="#fff" stroke-width="1.2"/>
          <path d="M4.5 7 V10.5 M7 7 V10.5 M9.5 7 V10.5" stroke="#2a2a22" stroke-width="1"/>
        </svg>
        <span class="cart-count">0</span>
      </span>
    </div>
  </header>

  <section class="hero-copy">
    <h1 class="hero-title">Velmorix</h1>
    <h2 class="hero-tagline">The Next Revolution in Cannabinoids</h2>
    <p class="hero-text">Velmorix is the first lab to be able to make the minor cannabinoids TCHP and CBDP in bulk batches. These canniboids were are 2 of the 150 cannabinoids found in the hemp plant and 2 of the ones found in the smallest amounts.</p>
    <a class="btn-learn" href="#">LEARN MORE
      <svg width="9" height="8" viewBox="0 0 9 8"><path d="M0 4 H7.5 M4.5 1 L7.5 4 L4.5 7" stroke="#fff" stroke-width="1.6" fill="none"/></svg>
    </a>
  </section>

  <svg class="hero-wave" viewBox="0 0 1200 100" preserveAspectRatio="none">
    <path d="M0 48 C220 95 520 98 760 58 C900 36 1060 26 1200 70 L1200 100 L0 100 Z" fill="rgba(255,255,255,0.35)"/>
    <path d="M0 58 C240 105 540 100 780 60 C920 38 1070 32 1200 78 L1200 100 L0 100 Z" fill="#ffffff"/>
  </svg>
</body>
</html>
```